Website for legal expungement services with button to qualify/disqualify potential clients

Brightfield Record Relief, LLC is a law firm focusing in legal expungement servcies (allowing people to erase criminal court records, police records, proseution files, etc). I want a more modern look which exudes confidence in the services. I am looking for a clean website that looks very polished. I want to keep the pages to a minimum, as I want the page not so much to answer questions, but to direct traffic to contact the law office. I would like the main focus point to be an button which would take a client through a series of questions to see if they would qualify for the services; this serves two purposes 1) to collect contact info for future marketing via email and 2) eliminate individuals who we are currently unable to help. A current theme that I have played around with are "Change so much, you'll need to reintroduce yourself" alongside a picture of a guys hand outstretched.
On the landing page, I would like a very brief and to the point explanation of what the service would be (i.e. "Leave your past in the past; expunge all your criminal records" ), followed by a list of benefits that it provides. (NB: included is a file "law post card-02" that includes the main benefits to expungement). Also included are two logo files for a more updated logo I currently use ("BRR Logo" and BRR Logo2") (NB: I'm open to revisions on this as well). Lastly, I've had two very minor 'ads' that I did ("postcard back" and "HVU Ad") that I like the idea of.

Target Market(s)

Middle/upper-middle class, mostly male, people with a criminal record or criminal accusation

Industry/Entity Type

Legal Services

Coding

Coded - Design and coding required

Requirements
Must have
• Button that attracts attention up front (possibly stand out coloring) to click to open up a series of questions to qualify/eliminate prospects, and simultaneously gather their info. Also, must be mobile friendly.

```html
<!DOCTYPE html>
<html lang="en">
<head>
<meta charset="utf-8">
<title>Brightfield Record Relief, LLC — Legal Expungement</title>
<link href="https://fonts.googleapis.com/css2?family=Cinzel:wght@400;600&family=Montserrat:wght@400;500;600;700&display=swap" rel="stylesheet">
<style>
:root{
  --navy:#0c3c78;
  --footer:#0b3b76;
  --ink:#3b4350;
  --pale:#eaf2fc;
  --bar:#3a3d42;
  --accent:#d99a1e;
  --accent-deep:#b97d0c;
  --white:#ffffff;
}
*{box-sizing:border-box;margin:0;padding:0}
html,body{width:1200px;height:3871px;overflow:hidden}
body{position:relative;background:var(--white);font-family:'Montserrat',sans-serif;color:var(--ink)}
.abs{position:absolute}
.serif{font-family:'Cinzel',serif}
.btn{position:absolute;display:flex;align-items:center;justify-content:center;font-size:12.5px;font-weight:500;text-decoration:none}
.btn-outline{border:1.5px solid var(--navy);color:var(--navy);background:var(--white)}
.btn-qualify{background:var(--accent);color:var(--white);font-size:15px;font-weight:700;letter-spacing:.5px;border-radius:3px;box-shadow:0 6px 18px rgba(185,125,12,.45);border-bottom:3px solid var(--accent-deep)}

/* brand name set as plain text */
.brand-name{font-family:'Cinzel',serif;font-weight:600;line-height:1.1;white-space:nowrap}

/* hero */
.hero{left:0;top:0;width:1200px;height:520px;background:linear-gradient(100deg,#b6bcc4 0%,#a9b0b9 45%,#c3c8cf 100%)}
.hero-brand{left:165px;top:44px;color:var(--navy);font-size:20px}
.hero-title{left:161px;top:146px;font-size:47px;line-height:54px;color:var(--white);font-weight:400}
.hero-title .lead{color:var(--navy)}
.hero-photo{left:690px;top:0;width:380px;height:520px;background:linear-gradient(180deg,#9aa3ae,#1d3358 70%,#172a4a)}

/* about */
.h2{font-family:'Cinzel',serif;color:var(--navy);font-weight:400;font-size:42px;font-variant:small-caps}
.about-title{left:161px;top:600px;font-size:46px}
.copy{font-size:12.5px;line-height:23px;color:var(--ink)}
.copy p+p{margin-top:9px}
.about-col{left:161px;top:662px;width:400px}
.about-wide{left:161px;top:1090px;width:878px}
.about-photo{left:601px;top:608px;width:599px;height:451px;border:7px solid var(--navy);border-right:none;border-radius:12px 0 0 12px;background:linear-gradient(135deg,#1b3f8c 0%,#3d7fd0 45%,#9cc6f2 60%,#183a72 100%)}

/* services */
.services-title{left:0;width:1200px;top:1425px;text-align:center}
.card{position:absolute;top:1565px;width:275px;height:377px;background:var(--white);box-shadow:0 4px 22px rgba(20,40,80,.1);border-radius:3px;text-align:center}
.card-icon{position:absolute;left:92px;top:-47px;width:90px;height:90px;border:1.5px solid var(--navy);background:var(--white);border-radius:2px;display:flex;align-items:center;justify-content:center}
.card-icon span{display:block;width:50px;height:50px;border-radius:50%;background:#dbe6f5}
.card h3{position:absolute;top:70px;left:0;width:100%;font-family:'Cinzel',serif;font-weight:400;font-size:18px;line-height:21px;color:var(--navy);font-variant:small-caps}
.card p{position:absolute;top:123px;left:26px;width:223px;font-size:12px;line-height:23px;color:var(--ink)}
.card .btn{left:77px;top:299px;width:120px;height:41px}

/* benefits */
.benefits{left:0;top:2037px;width:1200px;height:629px;background:var(--pale);overflow:hidden}
.benefits-scale{left:781px;top:216px;width:419px;height:413px;background:radial-gradient(ellipse at 60% 50%,#d5deea 0%,rgba(213,222,234,0) 70%)}
.benefits-title{left:0;width:1200px;top:80px;text-align:center;font-size:44px}
.benefits-intro{left:190px;width:820px;top:141px;text-align:center;font-size:11.5px;line-height:25.5px;color:var(--ink)}
.benefits-intro a{color:var(--navy)}
.ring{left:0;top:0}
.node{position:absolute;width:76px;height:76px;border-radius:50%;background:var(--white);box-shadow:0 3px 14px rgba(20,40,80,.15);display:flex;align-items:center;justify-content:center}
.node span{width:34px;height:34px;border-radius:50%;background:#d6e2f3}
.label{position:absolute;font-size:12px;line-height:25px;color:var(--ink)}
.label.r{text-align:right}
.center-name{left:440px;top:448px;width:320px;text-align:center;color:var(--navy);font-size:26px;line-height:32px}

/* records */
.records-photo{left:0;top:2756px;width:599px;height:413px;border-radius:0 12px 12px 0;background:linear-gradient(150deg,#7a6f66 0%,#c9c4bf 40%,#3f2c20 75%,#241811 100%)}
.records-title{left:638px;top:2786px;font-size:43px;line-height:50px}
.checklist{left:638px;top:2900px;list-style:none}
.checklist li{display:flex;align-items:center;height:33px;font-size:12.5px;color:var(--ink)}
.checklist svg{margin-right:12px}

/* call to action */
.cta-sky{left:0;top:3390px;width:1200px;height:237px;background:linear-gradient(180deg,#ffffff 0%,#d9dbde 35%,#8d939a 100%)}
.cta-title{left:0;width:1200px;top:3250px;text-align:center;font-size:36px;line-height:48px;color:#3a3f46;font-weight:400;font-variant:small-caps}
.cta .btn{left:511px;top:3350px;width:178px;height:40px}

/* footer */
.footer{left:0;top:3627px;width:1200px;height:200px;background:var(--footer)}
.foot-brand{left:398px;top:60px;color:var(--white);font-size:17px}
.seal{left:671px;top:38px;width:130px;height:53px;border-radius:6px;background:#e9ecef;border:2px solid #c7ccd2}
.contact{position:absolute;top:125px;display:flex;align-items:center;color:var(--white);font-size:13px;line-height:20px}
.contact .ico{width:38px;height:38px;border:1.5px solid var(--white);border-radius:50%;display:flex;align-items:center;justify-content:center;margin-right:14px}
.bottom-bar{left:0;top:3827px;width:1200px;height:44px;background:var(--bar);color:#e6e6e6;font-size:11.5px}
.bottom-bar p{position:absolute;left:162px;top:14px}
.social{position:absolute;top:9px;width:26px;height:26px;border:1.5px solid #e6e6e6;border-radius:50%}
</style>
</head>
<body>

<header class="abs hero">
  <div class="abs brand-name hero-brand">Brightfield Record Relief</div>
  <h1 class="abs serif hero-title"><span class="lead">CHANGE SO MUCH...</span><br>YOU'LL NEED TO<br>REINTRODUCE<br>YOURSELF</h1>
  <a class="btn btn-qualify" href="#qualify" style="left:161px;top:376px;width:230px;height:52px">See If You Qualify &rarr;</a>
  <div class="abs hero-photo" role="img" aria-label="Smiling man in a navy suit reaching out his hand for a handshake"></div>
</header>

<section class="about">
  <h2 class="abs h2 about-title">About Us</h2>
  <div class="abs copy about-col">
    <p>Welcome to Brightfield Record Relief, LLC, New Mexico's premier law firm for legal expungement. As the first law firm in the state dedicated exclusively to this area of law, we are proud to provide comprehensive legal services to individuals seeking to clear their criminal records. With a current success rate of over 99%, we have established ourselves as a trusted resource for individuals who believe in second chances.</p>
    <p>At Brightfield Record Relief, we firmly believe in the power of redemption and recognize that people can change. Our mission is to ensure that our clients are not defined by past mistakes or criminal accusations, but rather by their present and future potential. We understand the significant impact a criminal record can have on one's life, affecting employment prospects, housing opportunities, and personal relationships. Therefore, we are committed to helping our clients navigate the complex process of expungement with compassion, expertise, and a relentless dedication to their success.</p>
  </div>
  <div class="abs about-photo" role="img" aria-label="Lawyer signing a document with a glowing digital network overlay"></div>
  <div class="abs copy about-wide">
    <p>Our team of highly skilled attorneys possesses an in-depth understanding of the expungement laws and processes in New Mexico. We stay up-to-date with the latest legal developments to provide our clients with the most effective strategies tailored to their unique circumstances. With years of experience and a proven track record, we have successfully guided numerous individuals towards a fresh start, empowering them to overcome the burdens of their past and move forward with confidence.</p>
    <p>Client satisfaction is at the core of our practice, and we prioritize building strong relationships based on trust, empathy, and open communication. From the moment you reach out to us, you can expect personalized attention, honest advice, and unwavering support. We take the time to listen to your story, understand your goals, and develop a customized legal strategy that maximizes your chances of a successful expungement.</p>
    <p>Whether you are seeking to expunge a misdemeanor or a felony, our team at Brightfield Record Relief is here to guide you through the entire expungement process. We are committed to relentlessly pursuing justice on your behalf, protecting your rights, and advocating for your future. Let us help you clear your record and embrace a brighter tomorrow.</p>
  </div>
</section>

<section class="services">
  <h2 class="abs h2 services-title">Services We Provide</h2>
  <article class="card" style="left:161px">
    <div class="card-icon"><span role="img" aria-label="Head with checkmark icon"></span></div>
    <h3>Felony<br>Convictions</h3>
    <p>A felony conviction is extremely damaging to a person's quality of life and future prospects. We provide an opportunity for those who have completed their sentence and demonstrated rehabilitation to move forward with a fresh start.</p>
    <a class="btn btn-outline">Contact Us</a>
  </article>
  <article class="card" style="left:463px">
    <div class="card-icon"><span role="img" aria-label="Two people talking icon"></span></div>
    <h3>Misdemeanor<br>Convictions</h3>
    <p>Misdemeanor expungement offers individuals the opportunity to have their misdemeanor convictions cleared, providing benefits such as improved job prospects, housing opportunities, and a clean history.</p>
    <a class="btn btn-outline">Contact Us</a>
  </article>
  <article class="card" style="left:765px">
    <div class="card-icon"><span role="img" aria-label="Hands with scales of justice icon"></span></div>
    <h3>Non-Conviction<br>Accusations</h3>
    <p>Cleaning police reports through expungement provides individuals with the benefits of removing past accusations, allowing them to pursue employment, housing, and other opportunities without the burden of a tarnished record.</p>
    <a class="btn btn-outline">Contact Us</a>
  </article>
</section>

<section class="abs benefits">
  <div class="abs benefits-scale" role="img" aria-label="Faint scales of justice in the background"></div>
  <h2 class="abs h2 benefits-title">The Benefits of Expungement</h2>
  <p class="abs benefits-intro">Brightfield Record Relief is New Mexico's premier expungement law firm, dedicated solely to helping individuals clean their records since the passage of the 2020 expungement law. With a proven track record of success and a <a href="#">5-star rating on ReviewHub</a><br>we have transformed countless lives by providing effective, personalized expungement services.</p>
  <svg class="abs ring" width="1200" height="629" viewBox="0 0 1200 629" aria-hidden="true">
    <circle cx="600" cy="571" r="250" fill="none" stroke="#1a1a1a" stroke-width="3"/>
  </svg>
  <div class="node" style="left:507px;top:294px"><span role="img" aria-label="Hand with money icon"></span></div>
  <div class="node" style="left:620px;top:294px"><span role="img" aria-label="Stack of books icon"></span></div>
  <div class="node" style="left:402px;top:339px"><span role="img" aria-label="Document with pen icon"></span></div>
  <div class="node" style="left:714px;top:339px"><span role="img" aria-label="Insurance savings icon"></span></div>
  <div class="node" style="left:336px;top:421px"><span role="img" aria-label="Trophy icon"></span></div>
  <div class="node" style="left:778px;top:421px"><span role="img" aria-label="Privacy shield icon"></span></div>
  <div class="node" style="left:316px;top:523px"><span role="img" aria-label="Hand with percent coin icon"></span></div>
  <div class="node" style="left:808px;top:523px"><span role="img" aria-label="Apartment building icon"></span></div>

  <div class="label r" style="right:649px;top:245px">More &amp; Better Job Opprtunities<br>Leading To Higher Income</div>
  <div class="label" style="left:658px;top:245px">Better Education<br>Opportunities</div>
  <div class="label r" style="right:819px;top:352px">Removing The Stigma Of<br>Having A Criminal Record</div>
  <div class="label" style="left:819px;top:355px">Lower Insurance<br>Premiums</div>
  <div class="label r" style="right:882px;top:437px">Qualifying For Government<br>Assistance Programs</div>
  <div class="label" style="left:879px;top:437px">Protecting Your<br>Privacy</div>
  <div class="label r" style="right:909px;top:538px">Loan Qualification &amp;<br>Better Loan Rates</div>
  <div class="label" style="left:915px;top:538px">More Options For<br>Housing</div>

  <div class="abs brand-name center-name">Brightfield<br>Record Relief</div>
  <a class="btn btn-outline" style="left:539px;top:557px;width:120px;height:41px">Contact Us</a>
</section>

<section class="records">
  <div class="abs records-photo" role="img" aria-label="Hands signing papers beside a judge's gavel on a wooden desk"></div>
  <h2 class="abs h2 records-title">How Your Records<br>Are Seen By Public</h2>
  <ul class="abs checklist">
    <li><svg width="15" height="15" viewBox="0 0 16 16"><circle cx="8" cy="8" r="8" fill="#0c3c78"/><path d="M4.3 8.2l2.4 2.4 5-5" stroke="#fff" stroke-width="2" fill="none"/></svg>Public Reporting (www.statecourts.example)</li>
    <li><svg width="15" height="15" viewBox="0 0 16 16"><circle cx="8" cy="8" r="8" fill="#0c3c78"/><path d="M4.3 8.2l2.4 2.4 5-5" stroke="#fff" stroke-width="2" fill="none"/></svg>Police Reports</li>
    <li><svg width="15" height="15" viewBox="0 0 16 16"><circle cx="8" cy="8" r="8" fill="#0c3c78"/><path d="M4.3 8.2l2.4 2.4 5-5" stroke="#fff" stroke-width="2" fill="none"/></svg>State Department Of Public Safety</li>
    <li><svg width="15" height="15" viewBox="0 0 16 16"><circle cx="8" cy="8" r="8" fill="#0c3c78"/><path d="M4.3 8.2l2.4 2.4 5-5" stroke="#fff" stroke-width="2" fill="none"/></svg>District Attorney Prosecution Files</li>
    <li><svg width="15" height="15" viewBox="0 0 16 16"><circle cx="8" cy="8" r="8" fill="#0c3c78"/><path d="M4.3 8.2l2.4 2.4 5-5" stroke="#fff" stroke-width="2" fill="none"/></svg>Court Records</li>
  </ul>
  <a class="btn btn-outline" style="left:638px;top:3082px;width:118px;height:41px">Contact Us</a>
</section>

<section class="cta">
  <div class="abs cta-sky" role="img" aria-label="Black and white city skyline fading in from below"></div>
  <h2 class="abs serif cta-title">To See If You Qualify For Expungement Of<br>For Additional Information Contact Us</h2>
  <a class="btn btn-outline">Call Us : 555-014-2290</a>
</section>

<footer class="abs footer">
  <div class="abs brand-name foot-brand">Brightfield Record Relief</div>
  <div class="abs seal" role="img" aria-label="Secure connection badge"></div>
  <div class="contact" style="left:241px">
    <div class="ico"><svg width="16" height="20" viewBox="0 0 16 20"><path d="M8 1a6.5 6.5 0 0 0-6.5 6.5C1.5 12.5 8 19 8 19s6.5-6.5 6.5-11.5A6.5 6.5 0 0 0 8 1z" fill="none" stroke="#fff" stroke-width="1.6"/><circle cx="8" cy="7.5" r="2.3" fill="none" stroke="#fff" stroke-width="1.6"/></svg></div>
    <div>2418 Cedar Ridge Ave, Suite B,<br>Riverton, NM 87044</div>
  </div>
  <div class="contact" style="left:528px">
    <div class="ico"><svg width="18" height="18" viewBox="0 0 24 24"><path d="M6.6 10.8a15.1 15.1 0 0 0 6.6 6.6l2.2-2.2a1 1 0 0 1 1-.25 11.4 11.4 0 0 0 3.6.57 1 1 0 0 1 1 1V20a1 1 0 0 1-1 1A17 17 0 0 1 3 4a1 1 0 0 1 1-1h3.5a1 1 0 0 1 1 1 11.4 11.4 0 0 0 .57 3.6 1 1 0 0 1-.25 1z" fill="#fff"/></svg></div>
    <div>Phone<br>555-014-2290</div>
  </div>
  <div class="contact" style="left:753px">
    <div class="ico"><svg width="18" height="14" viewBox="0 0 18 14"><rect x="1" y="1" width="16" height="12" rx="1.5" fill="#fff"/><path d="M1.5 2l7.5 6 7.5-6" fill="none" stroke="#0b3b76" stroke-width="1.5"/></svg></div>
    <div>Email<br>info@harlowlegal.example</div>
  </div>
</footer>

<div class="abs bottom-bar">
  <p>(C) 2023 Brightfield Record Relief, LLC is a subsidiary of Harlow Legal Group, LLC.All rights reserved.</p>
  <span class="social" style="left:977px" aria-label="Social link"></span>
  <span class="social" style="left:1013px" aria-label="Social link"></span>
</div>

</body>
</html>
```